TrueLane Collision Repair Web Site

Create a web site that will inform my potential customers about the services I provide. We are a Automotive Collision repair business that uses the latest state of the art equipment, computerized paint matching highly trained technicians, have over 30 years experience. We work with all all insurance programs. Our Moto is "Fixed Right, The First Time, Every Time". TrueLane, The intelligent choice in collision repair.

Target Market(s)

People that have been in a auto collision, needs windshield replaced, people that drive 10 year or newer cars

Industry/Entity Type

Automotive

Coding

Coded - Design and coding required

Number of Pages Required

4 page

Font styles to use
Sans Serif

Requirements
Must have
• Logo, Place for Phone number, I need to be able to put the code in so I can use a tracking phone number
• site needs to be mobile ready or adaptive
• May want to have a photo of a high end car
• here is a web site for example with the pages that I want
• https://www.brisvaleautobody.example/online-repair-estimate,
• https://www.brisvaleautobody.example/schedule-appointment
• https://www.brisvaleautobody.example/collision-repair/auto-body-repair
• https://www.brisvaleautobody.example/contact
Nice to have
• Be great if the Car in the log could have the front damaged then have it fix in a animation. Not sure if could be done here

```html
<!DOCTYPE html>
<html lang="en">
<head>
<meta charset="utf-8">
<title>TrueLane Collision Repair</title>
<link rel="stylesheet" href="https://fonts.googleapis.com/css2?family=Cinzel:wght@400;700&family=Lato:ital,wght@0,400;0,700;1,400&display=swap">
<style>
:root{
  --blue:#1f57a8;
  --navy:#163c7a;
  --deep:#0f2d5c;
  --green:#8cc63f;
  --green-dark:#6fa52a;
  --red:#c8151b;
  --ink:#333333;
  --muted:#666666;
  --light:#f0f0f0;
  --charcoal:#3a3a3a;
  --card:#2a2a2a;
  --white:#ffffff;
}
*{box-sizing:border-box;margin:0;padding:0}
html,body{width:1200px;height:3543px;overflow:hidden}
body{font-family:"Lato",sans-serif;color:var(--ink);background:var(--white);position:relative}
section,header,footer,nav{position:absolute;left:0;width:1200px}

/* header */
.site-header{top:0;height:111px;background:var(--white)}
.brand{position:absolute;left:130px;top:28px;display:flex;align-items:center;gap:10px;font-family:"Cinzel",serif;font-weight:700;font-size:30px;color:var(--navy)}
.brand-dot{width:14px;height:14px;border-radius:50%;background:var(--green)}
.phone{position:absolute;left:763px;top:16px;display:flex;align-items:center;gap:8px;font-size:21px;color:var(--ink);white-space:nowrap}
.phone-icon{width:30px;height:30px;border-radius:50%;border:2px solid var(--ink);display:flex;align-items:center;justify-content:center}
.socials{position:absolute;left:958px;top:16px;display:flex;gap:6px}
.social{width:30px;height:30px;border-radius:50%;border:2px solid #555}
.btn-appointment{position:absolute;left:853px;top:61px;width:215px;height:34px;background:var(--green);color:var(--white);font-family:"Lato",sans-serif;font-weight:700;font-size:13px;text-transform:uppercase;display:flex;align-items:center;justify-content:center;white-space:nowrap;text-decoration:none;letter-spacing:0}

/* nav */
.main-nav{top:111px;height:42px;background:var(--blue);display:flex;justify-content:center;align-items:stretch}
.main-nav a{font-family:"Cinzel",serif;color:var(--white);text-decoration:none;font-size:16px;padding:0 28px;display:flex;align-items:center;border-right:1px solid rgba(255,255,255,.2);white-space:nowrap}
.main-nav a.active{background:var(--deep)}
.main-nav a:last-child{border-right:none}

/* hero */
.hero{top:153px;height:471px}
.hero-photo{position:absolute;inset:0;background:linear-gradient(120deg,#d9d0c2 0%,#9a8c7a 35%,#8b2a2f 60%,#5a1519 80%,#b8aa98 100%)}
.hero-caption{position:absolute;left:0;right:0;bottom:18px;text-align:center;color:var(--white);font-family:"Cinzel",serif;font-size:23px;line-height:33px;text-shadow:0 1px 3px rgba(0,0,0,.6)}
.hero-arrow{position:absolute;top:210px}
.hero-arrow.prev{left:32px}.hero-arrow.next{right:32px}

/* brands */
.brands{top:624px;height:182px;background:var(--light)}
.brand-name{position:absolute;top:72px;font-family:"Lato",sans-serif;font-weight:700;font-size:24px;color:#555;transform:translateX(-50%);letter-spacing:1px}
.brands .arrow{position:absolute;top:70px}

/* welcome */
.welcome{top:806px;height:555px;text-align:center}
.welcome h1{position:absolute;top:44px;left:0;right:0;font-family:"Cinzel",serif;font-weight:400;font-size:30px;color:var(--ink)}
.welcome h1 span{color:var(--blue)}
.rule{position:absolute;top:104px;left:380px;width:440px;height:1px;background:#ccc}
.rule-mark{position:absolute;top:96px;left:572px;width:56px;height:16px;background:var(--white);font-family:"Cinzel",serif;font-size:11px;color:#888}
.welcome p{position:absolute;top:146px;left:160px;width:880px;font-size:16px;line-height:28px;color:var(--muted)}
.motto{position:absolute;top:328px;transform:translateX(-50%);text-align:center}
.motto-circle{width:132px;height:132px;border-radius:50%;background:var(--navy);border:7px solid var(--green);box-shadow:0 4px 8px rgba(0,0,0,.25);display:flex;align-items:center;justify-content:center;margin:0 auto}
.motto-label{margin-top:18px;font-size:18px;color:var(--ink);white-space:nowrap}
.motto-arrow{position:absolute;top:382px}

/* services */
.services{top:1361px;height:564px;background:linear-gradient(180deg,#1a3f78 0%,#284f8d 50%,#173a70 100%);overflow:hidden}
.services-car{position:absolute;left:280px;top:90px;width:820px;height:470px;border-radius:300px 300px 40px 40px;background:radial-gradient(ellipse at 50% 50%,rgba(180,195,215,.45),rgba(40,70,120,0) 70%)}
.band{position:absolute;left:0;right:0;height:50px;display:flex;align-items:center;justify-content:center;font-family:"Cinzel",serif;font-size:28px;color:var(--white)}
.services .band{top:31px;background:linear-gradient(90deg,rgba(140,198,63,0) 10%,var(--green) 30%,var(--green) 70%,rgba(140,198,63,0) 90%)}
.service-node{position:absolute;width:118px;height:118px;border-radius:50%;background:var(--white);display:flex;align-items:center;justify-content:center;transform:translate(-50%,-50%)}
.badge{position:absolute;width:48px;height:48px;border-radius:50%;background:var(--red);color:var(--white);font-weight:700;font-size:20px;display:flex;align-items:center;justify-content:center;border:3px solid var(--white);transform:translate(-50%,-50%)}
.service-label{position:absolute;color:var(--white);font-size:26px;line-height:32px}
.hub{position:absolute;left:433px;top:430px;width:334px;height:170px;border-radius:167px 167px 0 0;background:rgba(15,40,80,.85);border:2px dashed rgba(255,255,255,.8);border-bottom:none;display:flex;align-items:center;justify-content:center;padding-top:20px;font-family:"Cinzel",serif;font-weight:700;font-size:36px;color:var(--white)}

/* estimate */
.estimate{top:1925px;height:503px}
.estimate-card{position:absolute;left:132px;top:54px;width:458px;height:359px;background:var(--card);border-radius:8px;box-shadow:0 10px 18px rgba(0,0,0,.35);padding:28px 40px}
.estimate-card h2{font-family:"Cinzel",serif;font-weight:400;color:var(--white);font-size:30px;text-align:center;margin-bottom:22px}
.fields{display:grid;grid-template-columns:1fr 1fr;gap:16px 14px}
.field{height:38px;border:1px solid #777;border-radius:3px;color:var(--white);font-size:14px;display:flex;align-items:center;justify-content:space-between;padding:0 12px;white-space:nowrap}
.btn-submit{display:flex;align-items:center;justify-content:center;margin:18px auto 0;width:188px;height:38px;background:var(--green);color:var(--white);font-weight:700;font-size:13px;border-radius:3px}
.safe{position:absolute;left:621px;top:78px;width:450px}
.safe h2{font-family:"Cinzel",serif;font-weight:400;color:var(--blue);font-size:26px;margin-bottom:18px}
.safe p{font-size:14px;line-height:23px;color:var(--ink);margin-bottom:23px}
.btn-more{display:inline-flex;align-items:center;justify-content:center;width:115px;height:32px;background:var(--navy);color:var(--white);font-size:12px;font-weight:700;border-radius:3px}

/* testimonials */
.testimonials{top:2428px;height:472px;background:var(--charcoal)}
.testimonials .band{top:42px;background:linear-gradient(90deg,rgba(80,80,80,0) 5%,#575757 30%,#575757 70%,rgba(80,80,80,0) 95%)}
.client-photo{position:absolute;width:142px;height:142px;border-radius:50%;border:5px solid var(--blue);background:linear-gradient(160deg,#9fb6cf,#3f5f86)}
.client-name{position:absolute;font-family:"Cinzel",serif;color:var(--white);font-size:17px;width:180px;text-align:center;white-space:nowrap}
.quote{position:absolute;width:300px;color:var(--white);font-style:italic;font-size:14px;line-height:27px}
.quote b{color:var(--green);font-size:26px;font-style:normal;vertical-align:-6px}
.links{position:absolute;display:flex;gap:22px;color:var(--white);font-size:13px;white-space:nowrap}
.testimonials .arrow{position:absolute;top:180px}

/* inquiry */
.inquiry{top:2900px;height:420px;background:linear-gradient(180deg,#1c4c93 0%,#24589f 50%,#1a4585 100%)}
.inquiry .band{top:50px;background:none}
.input{position:absolute;background:var(--navy);border:1px solid #4d79bb;border-radius:3px;color:var(--white);font-size:13px;padding:10px}
.btn-send{position:absolute;left:876px;top:125px;width:82px;height:76px;background:var(--green);color:var(--white);font-size:13px;font-weight:700;display:flex;align-items:center;justify-content:center;border-radius:3px}

/* footer */
.site-footer{top:3180px;height:363px;background:transparent}
.footer-wave{position:absolute;left:0;top:0}
.follow{position:absolute;top:28px;left:0;right:0;height:40px;display:flex;justify-content:center;align-items:center;gap:12px;color:var(--white);font-family:"Cinzel",serif;font-size:24px;white-space:nowrap}
.follow .label{margin-right:6px}
.follow .social{width:40px;height:40px;border:2px solid #4d79bb;background:var(--blue)}
.footer-col{position:absolute;top:112px;color:var(--white)}
.footer-col h3{font-weight:400;font-size:17px;margin-bottom:14px;white-space:nowrap}
.footer-col ul{list-style:none;font-size:14px;line-height:23px;white-space:nowrap}
.footer-col li::before{content:"› ";color:#aaa}
.contact-row{display:flex;gap:10px;font-size:14px;line-height:20px;margin-bottom:12px}
.map{position:absolute;left:576px;top:150px;width:246px;height:154px;background:linear-gradient(135deg,#dfe8d7,#c9d7e6 60%,#e8e2d2)}
.footer-brand{position:absolute;left:886px;top:175px;font-family:"Cinzel",serif;font-weight:700;font-size:28px;color:#cccccc}
.copyright{position:absolute;left:868px;top:250px;width:200px;color:var(--white);font-size:13px;line-height:20px}
</style>
</head>
<body>

<header class="site-header">
  <div class="brand"><span class="brand-dot"></span>TrueLane</div>
  <div class="phone">
    <span class="phone-icon"><svg width="14" height="14" viewBox="0 0 24 24"><path d="M6.6 10.8a15 15 0 0 0 6.6 6.6l2.2-2.2a1 1 0 0 1 1-.25 11.4 11.4 0 0 0 3.6.57 1 1 0 0 1 1 1V20a1 1 0 0 1-1 1A17 17 0 0 1 3 4a1 1 0 0 1 1-1h3.5a1 1 0 0 1 1 1c0 1.25.2 2.45.57 3.57a1 1 0 0 1-.25 1z" fill="#333"/></svg></span>
    123-456-7890
  </div>
  <div class="socials"><span class="social"></span><span class="social"></span><span class="social"></span></div>
  <a class="btn-appointment" href="https://www.brisvaleautobody.example/schedule-appointment">Schedule an Appointment</a>
</header>

<nav class="main-nav">
  <a class="active" href="#">Home</a>
  <a href="https://www.brisvaleautobody.example/online-repair-estimate">Need an estimate?</a>
  <a href="#">About Us</a>
  <a href="https://www.brisvaleautobody.example/collision-repair/auto-body-repair">Services</a>
  <a href="#">FAQ</a>
  <a href="#">Testimonials</a>
  <a href="https://www.brisvaleautobody.example/contact">Contact Us</a>
</nav>

<section class="hero">
  <div class="hero-photo" role="img" aria-label="Two technicians repairing the side panel of a red car inside a body shop"></div>
  <svg class="hero-arrow prev" width="40" height="60" viewBox="0 0 40 60"><path d="M32 4 6 30l26 26" fill="none" stroke="#fff" stroke-width="3"/></svg>
  <svg class="hero-arrow next" width="40" height="60" viewBox="0 0 40 60"><path d="M8 4l26 26L8 56" fill="none" stroke="#fff" stroke-width="3"/></svg>
  <div class="hero-caption">We have latest state of the art equipment, computerized paint<br>matching &amp; highly trained technicians with over 30 years experience</div>
</section>

<section class="brands">
  <svg class="arrow" style="left:82px" width="26" height="44" viewBox="0 0 26 44"><path d="M22 2 4 22l18 20" fill="none" stroke="#c4c4c4" stroke-width="3"/></svg>
  <span class="brand-name" style="left:187px">HALDEN</span>
  <span class="brand-name" style="left:354px">AURIQ</span>
  <span class="brand-name" style="left:569px">FERRANT</span>
  <span class="brand-name" style="left:765px">MIRAKO</span>
  <span class="brand-name" style="left:980px">BELLWOOD</span>
  <svg class="arrow" style="left:1092px" width="26" height="44" viewBox="0 0 26 44"><path d="M4 2l18 20L4 42" fill="none" stroke="#c4c4c4" stroke-width="3"/></svg>
</section>

<section class="welcome">
  <h1>Welcome To <span>TrueLane Collision Repair</span></h1>
  <div class="rule"></div>
  <div class="rule-mark">TrueLane</div>
  <p>Lorem ipsum dolor sit amet, consectetuer adipiscing elit, sed diam nonummy nibh euismod tincidunt ut laoreet dolore magna aliquam erat volutpat. Ut wisi enim ad minim veniam, quis nostrud exerci tation ullamcorper suscipit lobortis nisl ut aliquip ex ea commodo consequat. Duis autem vel eum iriure dolor in hendrerit in vulputate velit esse molestie consequat, vel illum dolore eu feugiat nulla facilisis. Ut wisi enim ad minim veniam, quis nostrud exerci tation ullamcorper suscipit lobortis nisl ut aliquip ex ea commodo consequat.</p>

  <div class="motto" style="left:347px">
    <div class="motto-circle"><svg width="62" height="50" viewBox="0 0 62 50"><path d="M8 30l6-14h34l6 14v12H8z" fill="#fff"/><circle cx="18" cy="40" r="5" fill="#163c7a"/><circle cx="44" cy="40" r="5" fill="#163c7a"/><rect x="17" y="20" width="28" height="8" fill="#163c7a"/></svg></div>
    <div class="motto-label">Fix Right</div>
  </div>
  <svg class="motto-arrow" style="left:430px" width="70" height="20" viewBox="0 0 70 20"><path d="M2 10h62m-8-7 8 7-8 7" fill="none" stroke="#aaa" stroke-width="1.5"/></svg>
  <div class="motto" style="left:598px">
    <div class="motto-circle"><svg width="54" height="54" viewBox="0 0 54 54"><circle cx="27" cy="27" r="22" fill="none" stroke="#fff" stroke-width="4"/><path d="M16 28l8 8 15-17" fill="none" stroke="#fff" stroke-width="5"/></svg></div>
    <div class="motto-label">First Time</div>
  </div>
  <svg class="motto-arrow" style="left:690px" width="70" height="20" viewBox="0 0 70 20"><path d="M2 10h62m-8-7 8 7-8 7" fill="none" stroke="#aaa" stroke-width="1.5"/></svg>
  <div class="motto" style="left:872px">
    <div class="motto-circle"><svg width="66" height="52" viewBox="0 0 66 52"><path d="M6 30l6-14h30l6 14v12H6z" fill="#fff"/><circle cx="50" cy="36" r="12" fill="#fff" stroke="#163c7a" stroke-width="3"/><path d="M44 36l5 5 8-9" fill="none" stroke="#163c7a" stroke-width="3"/></svg></div>
    <div class="motto-label">Every Time</div>
  </div>
</section>

<section class="services">
  <div class="services-car" role="img" aria-label="Rear view of a dark sports car behind the service diagram"></div>
  <div class="band">Auto Body Repair Service</div>
  <svg style="position:absolute;left:0;top:0" width="1200" height="564" viewBox="0 0 1200 564">
    <g fill="none" stroke="#fff" stroke-width="2" stroke-dasharray="4 5">
      <path d="M600 270v160"/>
      <path d="M400 350l110 44"/>
      <path d="M790 320l-65 88"/>
    </g>
    <g fill="#fff" stroke="#1a3f78" stroke-width="4">
      <circle cx="600" cy="324" r="10"/>
      <circle cx="462" cy="375" r="10"/>
      <circle cx="727" cy="376" r="10"/>
    </g>
  </svg>
  <div class="hub">TrueLane</div>

  <div class="service-node" style="left:347px;top:351px"><svg width="60" height="48" viewBox="0 0 60 48"><path d="M6 30l6-14h30l6 14v12H6z" fill="#222"/><circle cx="16" cy="40" r="4" fill="#fff"/><circle cx="38" cy="40" r="4" fill="#fff"/><path d="M42 6l12 12" stroke="#222" stroke-width="5"/></svg></div>
  <div class="badge" style="left:292px;top:302px">8</div>
  <div class="service-label" style="left:162px;top:330px">Collision<br>Repair</div>

  <div class="service-node" style="left:600px;top:210px"><svg width="60" height="44" viewBox="0 0 60 44"><circle cx="20" cy="22" r="14" fill="none" stroke="#222" stroke-width="6"/><path d="M34 22h22" stroke="#222" stroke-width="7"/></svg></div>
  <div class="badge" style="left:546px;top:164px">1</div>
  <div class="service-label" style="left:676px;top:176px">Frame<br>Repair</div>

  <div class="service-node" style="left:838px;top:316px"><svg width="50" height="50" viewBox="0 0 50 50"><path d="M10 40 36 14" stroke="#222" stroke-width="8" stroke-linecap="round"/><circle cx="38" cy="12" r="8" fill="none" stroke="#222" stroke-width="5"/></svg></div>
  <div class="badge" style="left:872px;top:370px">2</div>
  <div class="service-label" style="left:896px;top:300px">Alignment</div>
</section>

<section class="estimate">
  <form class="estimate-card" action="https://www.brisvaleautobody.example/online-repair-estimate">
    <h2>Need an Estimate?</h2>
    <div class="fields">
      <div class="field">Location <span>⌄</span></div>
      <div class="field">Year <span>⌄</span></div>
      <div class="field">Make <span>⌄</span></div>
      <div class="field">Model <span>⌄</span></div>
      <div class="field">Body Style <span>⌄</span></div>
      <div class="field">VIN</div>
      <div class="field">Insurance Company <span>⌄</span></div>
      <div class="field">Agent <span>⌄</span></div>
    </div>
    <div class="btn-submit">SUBMIT</div>
  </form>
  <div class="safe">
    <h2>Is your car safe to drive?</h2>
    <p>First, we hope that no one was injured in the unfortunate event that led you to search for a collision repair facility and we are glad you found us. Now we want to make sure we can help you mitigate any further loss or property or worse yet physical harm.</p>
    <p>Your car was just involved in a collision and depending on how severe the accident was it is possible that one or more of the many systems the manufacture of your vehicle has designed into your vehicle are no longer able to protect you if you get into another accident before proper repairs have been made.</p>
    <span class="btn-more">READ MORE</span>
  </div>
</section>

<section class="testimonials">
  <div class="band">Client Testimonials</div>
  <svg class="arrow" style="left:62px" width="28" height="100" viewBox="0 0 28 100"><path d="M24 2 4 50l20 48" fill="none" stroke="#fff" stroke-width="2"/></svg>
  <svg class="arrow" style="left:1112px" width="28" height="100" viewBox="0 0 28 100"><path d="M4 2l20 48L4 98" fill="none" stroke="#fff" stroke-width="2"/></svg>

  <div class="client-photo" style="left:137px;top:156px" role="img" aria-label="Portrait of client Dale Morrow"></div>
  <div class="client-name" style="left:118px;top:320px">- Dale Morrow</div>
  <p class="quote" style="left:290px;top:158px"><b>❝</b> Lorem ipsumn sit amet the co adipiscli tsedudml eiusmo dtepor is a incidiunt ut la dolore ma aliquamni kni this enim nim veni exercitation ullamco lorem ips sdlitnol ameti co adipiscig elitsed do eiusmod. <b>❞</b></p>
  <div class="links" style="left:288px;top:383px"><span>Local Listing</span><span>Ratings</span><span>Reviews</span></div>

  <div class="client-photo" style="left:625px;top:156px" role="img" aria-label="Portrait of client Owen Pratt"></div>
  <div class="client-name" style="left:606px;top:320px">- Owen Pratt</div>
  <p class="quote" style="left:786px;top:158px"><b>❝</b> Lorem ipsumn sit amet the co adipiscli tsedudml eiusmo dtepor is a incidiunt ut la dolore ma aliquamni kni this enim nim veni exercitation ullamco lorem ips sdlitnol ameti co adipiscig elitsed do eiusmod. <b>❞</b></p>
  <div class="links" style="left:786px;top:383px"><span>Local Listing</span><span>Ratings</span><span>Reviews</span></div>
</section>

<section class="inquiry" role="img" aria-label="Blue-tinted background of cars in a repair bay">
  <div class="band">Quick Inquiry</div>
  <div class="input" style="left:241px;top:125px;width:243px;height:38px">Name</div>
  <div class="input" style="left:241px;top:168px;width:243px;height:38px">Email Address</div>
  <div class="input" style="left:494px;top:125px;width:373px;height:81px">Message</div>
  <div class="btn-send">SEND</div>
</section>

<footer class="site-footer">
  <svg class="footer-wave" width="1200" height="363" viewBox="0 0 1200 363">
    <path d="M0 84C200 80 330 118 520 96S860 72 1000 92 1120 100 1200 86V363H0z" fill="#000"/>
    <path d="M0 84C200 80 330 118 520 96S860 72 1000 92 1120 100 1200 86" fill="none" stroke="#8cc63f" stroke-width="5"/>
  </svg>
  <div class="follow"><span class="label">Follow Us</span><span class="social"></span><span class="social"></span><span class="social"></span></div>

  <div class="footer-col" style="left:132px">
    <h3>Quick Links</h3>
    <ul><li>Home</li><li>Need an estimate?</li><li>About Us</li><li>Services</li><li>FAQ</li><li>Testimonials</li><li>Contact Us</li></ul>
  </div>
  <div class="footer-col" style="left:324px;width:220px">
    <h3>Contact Detail</h3>
    <div class="contact-row"><svg width="14" height="18" viewBox="0 0 14 18"><path d="M7 0a7 7 0 0 0-7 7c0 5 7 11 7 11s7-6 7-11a7 7 0 0 0-7-7z" fill="#fff"/><circle cx="7" cy="7" r="2.5" fill="#000"/></svg><span>Lorem ipsum dolor sit nil, consectetuer adipiscing elit, sed diam.(1234)</span></div>
    <div class="contact-row"><svg width="14" height="14" viewBox="0 0 24 24"><path d="M6.6 10.8a15 15 0 0 0 6.6 6.6l2.2-2.2a1 1 0 0 1 1-.25 11.4 11.4 0 0 0 3.6.57 1 1 0 0 1 1 1V20a1 1 0 0 1-1 1A17 17 0 0 1 3 4a1 1 0 0 1 1-1h3.5a1 1 0 0 1 1 1c0 1.25.2 2.45.57 3.57a1 1 0 0 1-.25 1z" fill="#fff"/></svg><b>(123) 456 7890</b></div>
    <div class="contact-row"><svg width="14" height="14" viewBox="0 0 14 14"><rect x="1" y="4" width="12" height="8" fill="#fff"/><rect x="3" y="1" width="8" height="3" fill="#fff"/></svg><b>(123) 456 7890</b></div>
    <div class="contact-row"><svg width="14" height="12" viewBox="0 0 14 12"><rect x="0.5" y="0.5" width="13" height="11" fill="none" stroke="#fff"/><path d="M1 1l6 5 6-5" fill="none" stroke="#fff"/></svg><span>info@truelane.example</span></div>
  </div>
  <div class="footer-col" style="left:576px"><h3>Location</h3></div>
  <div class="map" role="img" aria-label="Street map showing the shop location in Harbor City">
    <svg width="246" height="154" viewBox="0 0 246 154"><path d="M121 60a9 9 0 0 0-9 9c0 7 9 16 9 16s9-9 9-16a9 9 0 0 0-9-9z" fill="#c8151b"/><circle cx="121" cy="69" r="3" fill="#fff"/></svg>
  </div>
  <div class="footer-brand">TrueLane</div>
  <div class="copyright">Copyright 2016 TrueLane Collision Repair. All rights reserved.</div>
</footer>

</body>
</html>
```